Deckblatt für Word-Vorlagen für Sachverständigen und Gutachter für stationäre Gaswarnanlagen
Zielgruppe
Ich bin Sachverständiger und Gutachter für stationäre Gaswarnanlagen. Dies kann man sich vorstellen wie eine Brandmeldeanlage nur für Gase, also Bereich Mess- und Regeltechnik gemischt mit Sicherheitstechnik und dies rein als Sachverständiger.
Meine Zielgruppe sind rein nur Firmen und davon meistens Großkonzerne. Mein Erscheinungsbild muss als Wertig, Seriös und Teuer sein.
Aufgabenstellung
Ich benötige nur ein neues Deckblatt für Word-Vorlagen.
Das Deckblatt ist rein für meine Gutachten und Beurteilungen, sollte also nicht 'verspielt' sein.
Anbei die alte Version mit einer Office Vorlage und den Daten welche ich immer eintragen muss. Zusätzlich anbei meine neue Power Point Masterfolien-Vorlage, rein als Info. Das Deckblatt, wie auch alle späteren Seiten, sollen das Wasserzeichen (rundes Logo) behalten.

```html
<!DOCTYPE html>
<html lang="de">
<head>
<meta charset="utf-8">
<title>Auftrags-Gutachten – Deckblatt</title>
<link href="https://fonts.googleapis.com/css2?family=Source+Sans+3:wght@400;700&display=swap" rel="stylesheet">
<style>
  :root {
    --bg-deep: #0d1724;
    --bg-mid: #1c2d42;
    --bg-accent: #2a4670;
    --band-blue: #2e4078;
    --band-grey: #7a7a7a;
    --text: #ffffff;
    --card: rgba(255, 255, 255, 0.12);
  }
  * { margin: 0; padding: 0; box-sizing: border-box; }
  html, body { width: 844px; height: 1200px; overflow: hidden; background: var(--bg-deep); }
  .cover {
    position: relative; width: 844px; height: 1200px; overflow: hidden;
    font-family: "Source Sans 3", sans-serif; color: var(--text);
  }
  .backdrop {
    position: absolute; inset: 0;
    background:
      radial-gradient(circle at 48% 32%, var(--bg-accent) 0%, rgba(42, 70, 112, 0) 32%),
      radial-gradient(ellipse at 50% 45%, var(--bg-mid) 0%, var(--bg-deep) 80%);
  }
  .title-band { position: absolute; left: 0; top: 0; }
  .title {
    position: absolute; left: 0; width: 844px; top: 433px; text-align: center;
    font-size: 60px; font-weight: 700; line-height: 80px; letter-spacing: 0.3px;
  }
  .expert {
    position: absolute; left: 0; width: 844px; top: 588px; text-align: center;
    font-size: 22px; font-weight: 700; line-height: 32px;
  }
  .report-no {
    position: absolute; left: 0; width: 844px; top: 708px; text-align: center;
    font-size: 23px; font-weight: 700; line-height: 32px;
  }
  .info-card {
    position: absolute; top: 862px; width: 336px; height: 209px;
    background: var(--card); border-radius: 28px; text-align: center;
  }
  .info-card.client { left: 67px; }
  .info-card.site { left: 446px; }
  .info-card h2 { margin-top: 52px; font-size: 20px; font-weight: 700; line-height: 26px; }
  .info-card p { margin-top: 13px; font-size: 16px; line-height: 20.5px; }
  .contact-item {
    position: absolute; top: 1148px; display: flex; align-items: center; gap: 8px;
    font-size: 16px; line-height: 22px;
  }
  .contact-item.address { left: 41px; }
  .contact-item.mail { left: 381px; }
  .contact-item.phone { left: 652px; }
  .contact-item svg { fill: var(--text); flex: none; }
</style>
</head>
<body>
<main class="cover">
  <div class="backdrop" role="img" aria-label="Dunkelblauer Hintergrund mit leuchtenden Leiterbahn-Linien, Rautenraster und rundem Wasserzeichen-Logo"></div>

  <svg class="title-band" width="844" height="1200" viewBox="0 0 844 1200" aria-hidden="true">
    <path d="M300,468 Q300,446 322,446 L742,426 Q765,425 765,448 L765,510 Q765,532 742,532 L322,532 Q300,532 300,510 Z" fill="var(--band-grey)"/>
    <path d="M83,443 Q83,421 105,421 L526,421 Q548,421 548,443 L548,470 Q548,486 530,488 L105,527 Q83,529 83,507 Z" fill="var(--band-blue)"/>
  </svg>

  <h1 class="title">AUFTRAGS-GUTACHTEN</h1>

  <div class="expert">
    <p>Lorenz Valtmann</p>
    <p>BVGP-geprüfter Sachverständiger für Gaswarntechnik</p>
    <p>Fachkraft für Explosionsschutz</p>
  </div>

  <p class="report-no">Gutachten-Nr. 1202/001-01 vom 19. Januar 2021</p>

  <section class="info-card client">
    <h2>Auftraggeber</h2>
    <p>Agrarhandel Westmark eG<br>Lindenhofer Str. 7b<br>D-50412 Köln</p>
  </section>
  <section class="info-card site">
    <h2>Standort</h2>
    <p>Pflanzenschutzmittellager<br>Kanalweg 42<br>D-41472 Neuss</p>
  </section>

  <footer>
    <span class="contact-item address"><svg width="14" height="20" viewBox="0 0 14 20"><path d="M7 0C3 0 0 3 0 7c0 5 7 13 7 13s7-8 7-13c0-4-3-7-7-7zm0 9.5A2.5 2.5 0 1 1 7 4.5a2.5 2.5 0 0 1 0 5z"/></svg>Brunnengasse 9, 35519 Rockenfeld</span>
    <span class="contact-item mail"><svg width="22" height="16" viewBox="0 0 22 16"><path d="M0 0h22v16H0z"/><path d="M1 1 11 9 21 1" fill="none" stroke="var(--bg-deep)" stroke-width="1.6"/></svg>kontakt@gaspruef-kanzlei.de</span>
    <span class="contact-item phone"><svg width="20" height="20" viewBox="0 0 20 20"><path d="M4 1l3 0 2 5-2.5 1.5a11 11 0 0 0 6 6L14 11l5 2v3c0 1.5-1.5 3-3 3C8 19 1 12 1 4c0-1.5 1.5-3 3-3z"/></svg>06004/51836-0</span>
  </footer>
</main>
</body>
</html>
```